Conspiracy - Drama MOVIE POSTER

movie poster for a film in development

The movie is about a physics professor who discovers explosives in the dust from the harbor exchange plaza complex that were destroyed on 9/11 - conspiracy/drama -

the title of the movie is DEEP ECHO

the attached photos are just to start dialog - not at all in love with them

the main character has a wis and a son who would be apex 6 years old - his obsession will strain his relationships

a key scene in the movie will be his students raising a flag upside-down - in his honor

working tag line: TRUTH IS FOR THOSE WHO SEEK IT

Target Market(s)

would just like a fresh modern look - audience is, of course, 18 -35 and I think it lends itself to Male

Industry/Entity Type

Film Production

Logo Text

DEEP ECHO

Font styles to use
Sans Serif

Requirements
Must have
• title
• space at bottom for info like actors and cast
Nice to have
• I have had work done on this before and one version I thought was clever was to make the last to "L's" the granite halls.
• actual photo of lead actors - stock image of course (I will pay for additional exp) the lead is male - late thirties / early forties - professor - a young Gil Marston
Should not have
• explosions - the movie is about the conflict in relationships - it is not a political thriller - more family drama

```html
<!DOCTYPE html>
<html lang="en">
<head>
<meta charset="utf-8">
<title>DEEP ECHO — Poster</title>
<link rel="stylesheet" href="https://fonts.googleapis.com/css2?family=Antonio:wght@100;400&display=swap">
<style>
  :root {
    --backdrop: #111820;
    --paper: #ffffff;
    --ink: #111111;
    --steel-blue: #2f5f9e;
    --deep-blue: #14294a;
    --pale-skin: #e9dcd8;
  }
  html, body {
    margin: 0;
    padding: 0;
    width: 1200px;
    height: 1200px;
    overflow: hidden;
    background: var(--backdrop);
  }
  .canvas {
    position: relative;
    width: 1200px;
    height: 1200px;
    background: var(--backdrop);
  }
  .poster {
    position: absolute;
    left: 198px;
    top: 0;
    width: 806px;
    height: 1200px;
    background: var(--paper);
    overflow: hidden;
  }
  .poster-art {
    position: absolute;
    inset: 0;
    width: 806px;
    height: 1200px;
  }
  .title {
    font-family: "Antonio", sans-serif;
    font-weight: 100;
    font-size: 178px;
    fill: var(--ink);
    text-anchor: middle;
  }
  .credits {
    font-family: "Antonio", sans-serif;
    font-weight: 400;
    font-size: 14px;
    fill: var(--ink);
    text-anchor: middle;
  }
</style>
</head>
<body>
<div class="canvas">
  <div class="poster">
    <svg class="poster-art" viewBox="0 0 806 1200" xmlns="http://www.w3.org/2000/svg">
      <defs>
        <linearGradient id="lead-portrait-tone" x1="0" y1="0" x2="0" y2="1">
          <stop offset="0" stop-color="#5a4a40"/>
          <stop offset="0.12" stop-color="#cfc2bc"/>
          <stop offset="0.45" stop-color="var(--pale-skin)"/>
          <stop offset="0.7" stop-color="#7d9bc7"/>
          <stop offset="0.85" stop-color="var(--steel-blue)"/>
          <stop offset="1" stop-color="var(--deep-blue)"/>
        </linearGradient>
      </defs>

      <text class="title" x="403" y="238" textLength="676" lengthAdjust="spacing">DEEP ECHO</text>

      <g class="lead-portrait" role="img" aria-label="Portrait of the lead actor in a blue suit, his chest dissolving into the receding facade lines of the granite halls">
        <path d="M0 898 C90 850 180 820 270 775 L270 740 C250 640 240 520 248 440 C260 350 320 308 398 308 C476 308 540 350 552 440 C560 520 550 640 536 740 L536 775 C626 820 716 850 806 898 L806 1100 L0 1100 Z" fill="url(#lead-portrait-tone)"/>
      </g>

      <g class="credit-block">
        <text class="credits" x="400" y="1116" textLength="786" lengthAdjust="spacing">TRUTH IS FOR THOSE WHO SEEK IT STARRING GIL MARSTON</text>
        <text class="credits" x="400" y="1138" textLength="644" lengthAdjust="spacing">DIRECTED BY NORA VALE WRITTEN BY OWEN PRICE</text>
        <text class="credits" x="400" y="1161" textLength="731" lengthAdjust="spacing">MUSIC BY LENA HART EDITED BY SAM COLE PRODUCED BY RUTH ADAIR</text>
        <text class="credits" x="400" y="1183" textLength="603" lengthAdjust="spacing">COMING SOON TO SELECT THEATERS</text>
      </g>
    </svg>
  </div>
</div>
</body>
</html>
```